Northfield Energy Product Distribution Brochure

We are looking to have our current brochure for our customers completely redesigned...the idea is to present the relevant information in an attractive way . Our website is northfieldenergy-example.com where you can find more information about us. We have included a file with a rough idea of the page order and what each should include but feel free to adapt based on design. The example provided is only for context and doesnt have to be maintained. We will be using the brochure both digitally and in print form. As long as it reads easily and is eye catching, the design can be horizontal or vertical.Final deliverable should be indesign file.

"Our Brands" page: should be limited to one page (space being enough) where it has the header for each one (for example diesel generators) space for one or two lines of text and then the corresponding logos for each of the five categories
Updates

For those asking: the "our brands" page should be a single page layout where there is a header with the corresponding section and space for maybe one line of text followed by the two logos for that category. Each of the product pages should be similar in fashion to the one in the document attached: a photo of the product with some white space and space for the text to be included. We will be posting additional examples today

Target Market(s)

We want to present it to customers both digitally and in print so they can see our products

Industry/Entity Type

Power Generation

Font styles to use
Serif

Requirements
Must have
• Eye catching and able to present the information in a presentable fashion. Rest is up to you.
Nice to have
• Should incorporate the colors of our logo but can also add other depending on design

```html
<!DOCTYPE html>
<html lang="en">
<head>
<meta charset="utf-8">
<title>Northfield Energy – Brochure Spread</title>
<link rel="stylesheet" href="https://fonts.googleapis.com/css2?family=Michroma&family=Montserrat:wght@400;500;600;800&display=swap">
<style>
  :root{
    --bg:#d9dcd8;
    --paper:#ffffff;
    --navy:#232a8c;
    --ink:#3a3a3a;
    --bar:#e4e4e6;
    --photo-dark:#2c2b29;
    --photo-light:#8d8a85;
    --panel:rgba(16,15,14,0.9);
    --yellow:#f2d21b;
    --cyan:#3fb8dc;
    --dg:#1aa9e0;
    --ts:#8e44a9;
    --ac:#e0312f;
    --ap:#f2b81c;
    --gc:#3fae4a;
  }
  *{box-sizing:border-box;margin:0;padding:0}
  html,body{width:1200px;height:960px;overflow:hidden;background:var(--bg)}
  body{font-family:"Montserrat",sans-serif;position:relative}
  .spread{position:absolute;left:40px;top:160px;width:1120px;height:640px;box-shadow:0 18px 40px rgba(0,0,0,.25);overflow:hidden}
  .photo{position:absolute;inset:0;background:linear-gradient(135deg,var(--photo-light) 0%,#5d5b57 35%,var(--photo-dark) 70%,#4a4844 100%)}
  .page-curve{position:absolute;left:0;top:0;width:560px;height:640px}
  .fold{position:absolute;left:559px;top:0;width:2px;height:640px;background:rgba(0,0,0,.25)}
  .index{position:absolute;left:0;top:0;width:560px;height:640px}
  .index-title{position:absolute;left:64px;top:130px;font-family:"Michroma",sans-serif;font-size:26px;color:var(--navy);letter-spacing:1px}
  .toc{position:absolute;left:70px;top:190px;width:300px;list-style:none}
  .toc li{display:flex;justify-content:space-between;align-items:center;height:30px;padding:0 6px;font-size:12px;text-transform:uppercase;color:var(--ink);letter-spacing:.3px}
  .toc li:nth-child(even){background:var(--bar)}
  .toc .num{font-weight:600;font-size:11px}
  .products{position:absolute;left:140px;top:345px;width:232px;list-style:none}
  .products li{display:flex;justify-content:space-between;align-items:center;height:21px;padding:0 6px 0 10px;font-size:11.5px;color:#fff}
  .products b{font-weight:800;margin-right:4px}
  .p-dg{background:var(--dg)}.p-ts{background:var(--ts)}.p-ac{background:var(--ac)}.p-ap{background:var(--ap)}.p-gc{background:var(--gc)}
  .distributors{position:absolute;left:96px;top:470px;width:276px;display:flex;justify-content:space-between;font-size:12px;color:var(--ink);text-transform:uppercase}
  .distributors .num{font-weight:600;font-size:11px}
  .folio{position:absolute;left:40px;top:600px;font-size:7px;color:#888}
  .about{position:absolute;left:600px;top:70px;width:480px;height:460px;background:var(--panel);padding:46px 40px}
  .about h2{font-family:"Michroma",sans-serif;font-weight:400;font-size:22px;color:var(--yellow);letter-spacing:1px}
  .about p{margin-top:10px;font-size:8px;line-height:1.45;color:#e8e8e8;width:380px}
  .stats{display:grid;grid-template-columns:repeat(4,92px);column-gap:10px;row-gap:22px;margin-top:26px}
  .stat{display:flex;flex-direction:column;align-items:center;text-align:center}
  .ring{width:80px;height:80px;border:2px solid var(--cyan);border-radius:50%;display:flex;align-items:center;justify-content:center;color:#fff;font-weight:800;font-size:18px}
  .ring svg{width:48px;height:48px}
  .label{margin-top:6px;font-size:7.5px;font-weight:700;color:var(--yellow);line-height:1.2}
</style>
</head>
<body>
<div class="spread">
  <div class="photo" role="img" aria-label="Black and white aerial photo of the company headquarters building and grounds"></div>
  <svg class="page-curve" viewBox="0 0 560 640" aria-hidden="true">
    <path d="M0 0 H250 C300 180 420 420 560 640 H0 Z" fill="var(--paper)"/>
  </svg>
  <div class="fold"></div>

  <section class="index">
    <h1 class="index-title">INDEX</h1>
    <ul class="toc">
      <li><span>About our company</span><span class="num">3</span></li>
      <li><span>Our team</span><span class="num">4</span></li>
      <li><span>Our brands</span><span class="num">5</span></li>
      <li><span>Our stock</span><span class="num">6</span></li>
      <li><span>Our products</span><span class="num">7</span></li>
    </ul>
    <ul class="products">
      <li class="p-dg"><span><b>DG</b>Diesel Generators</span><span>8</span></li>
      <li class="p-ts"><span><b>TS</b>Transfer Switches</span><span>10</span></li>
      <li class="p-ac"><span><b>AC</b>Alternators</span><span>12</span></li>
      <li class="p-ap"><span><b>AP</b>Alternator Parts</span><span>14</span></li>
      <li class="p-gc"><span><b>GC</b>Generator Controls</span><span>16</span></li>
    </ul>
    <div class="distributors"><span>Our distributors</span><span class="num">19</span></div>
    <div class="folio">2</div>
  </section>

  <section class="about">
    <h2>ABOUT OUR COMPANY</h2>
    <p>Bus, commodiandis as debitatem aspider ferrum acest, ullab idit, sintia verovit il initis volupta quis excepta spissimus et fuga. Et omnis aut autetur aut poribus apeditatur sus doluptur, nossequi rem hit et fugiae sanis ut poriae. Nam autecte</p>
    <div class="stats">
      <div class="stat"><div class="ring">20+</div><div class="label">years industry<br>experience</div></div>
      <div class="stat"><div class="ring">$4M+</div><div class="label">product inventory</div></div>
      <div class="stat"><div class="ring">100%</div><div class="label">original components</div></div>
      <div class="stat"><div class="ring" style="font-size:15px">10,000+</div><div class="label">Customers served</div></div>

      <div class="stat"><div class="ring"><svg viewBox="0 0 48 48"><g stroke="#fff" stroke-width="1.5"><line x1="24" y1="24" x2="6" y2="20"/><line x1="24" y1="24" x2="42" y2="18"/><line x1="24" y1="24" x2="10" y2="40"/><line x1="24" y1="24" x2="40" y2="38"/><line x1="24" y1="24" x2="24" y2="44"/></g><g fill="#fff"><circle cx="24" cy="12" r="5"/><path d="M17 26 Q24 16 31 26 Z"/><circle cx="6" cy="20" r="2.5"/><circle cx="42" cy="18" r="2.5"/><circle cx="10" cy="40" r="2.5"/><circle cx="40" cy="38" r="2.5"/><circle cx="24" cy="44" r="2.5"/></g></svg></div><div class="label">Master Distributors</div></div>
      <div class="stat"><div class="ring"><svg viewBox="0 0 48 48"><path d="M24 6 L44 24 H38 V42 H28 V30 H20 V42 H10 V24 H4 Z" fill="#fff"/></svg></div><div class="label">Single source<br>solution</div></div>
      <div class="stat"><div class="ring"><svg viewBox="0 0 48 48"><ellipse cx="17" cy="20" rx="14" ry="9" fill="#fff"/><path d="M10 27 L8 34 L16 28 Z" fill="#fff"/><ellipse cx="32" cy="26" rx="14" ry="9" fill="#ddd"/><path d="M38 33 L41 40 L33 34 Z" fill="#ddd"/></svg></div><div class="label">Fully bilingual staff</div></div>
      <div class="stat"><div class="ring"><svg viewBox="0 0 48 48"><circle cx="24" cy="24" r="17" fill="#fff"/><path d="M16 24 L22 31 L34 15" stroke="#1a1918" stroke-width="3.5" fill="none" stroke-linecap="round"/></svg></div><div class="label">Worldwide shipping</div></div>
    </div>
  </section>
</div>
</body>
</html>
```